Software company WebSite Design (enterprise level SW, Mobile apps, HW prototypes)

We need design for our new webpages. We got new logo and new business cards and we need webdesign which will be match with those two.
We are dealing with corporate level software development - enterprise level portals, development of optimalization SW, route planning optimalizations. For a few months we are developing mobile applications for companies.
IMPORTANT is to express the cutting edge technological company.

Target Market(s)

IT company customers

Industry/Entity Type

Business

Number of Pages Required

2 page

Requirements
Must have
• Project needs to have landing page and product detail page. Design needs to be created including full font and example images as there would be a real webpage. Design should be clean, modern and expressing hi-tech level of the company.
• Example of well designer web pages - www.quorvelt.com, www.brandissa.com - We like the font formatting and font designs (colors, placing, etc - its professional).
• Attached image contains screenshot from old web landing page. It contains basic sections of our business (Simulation Tools, Enterprise Intranet Systems, Hi-tech web presentations, Supporting Enterprise services - Optimalization and logistics monitoring)

```html
<!DOCTYPE html>
<html lang="en">
<head>
<meta charset="utf-8">
<title>Norvex Solutions — Enterprise Software</title>
<link href="https://fonts.googleapis.com/css2?family=Lato:wght@300;400;700&display=swap" rel="stylesheet">
<style>
  :root {
    --ink: #3d3d3f;
    --ink-soft: #5a5a5d;
    --ink-muted: #77777a;
    --page: #e6e6e7;
    --page-alt: #dcdcde;
    --brand-blue: #2c9ad3;
    --brand-red: #d63e2a;
    --brand-orange: #e97f2e;
    --backdrop: #8a8a8c;
  }
  * { box-sizing: border-box; margin: 0; padding: 0; }
  html, body { width: 1200px; height: 900px; overflow: hidden; }
  body {
    font-family: "Lato", sans-serif;
    color: var(--ink);
    background: var(--page);
  }
  .site { width: 1200px; height: 900px; position: relative; }

  /* Hero */
  .hero { position: relative; height: 560px; overflow: hidden; }
  .hero-photo {
    position: absolute; inset: 0;
    background: linear-gradient(120deg, #d5d5d7 0%, #c9c8c8 35%, #d2cfcd 60%, #dcdbdc 100%);
  }
  .hero-veil {
    position: absolute; inset: 0;
    background: rgba(232, 232, 233, 0.55);
  }
  .nav {
    position: relative; display: flex; align-items: center;
    height: 76px; padding: 0 130px 0 160px;
  }
  .brand { display: flex; align-items: center; gap: 10px; }
  .brand-mark { width: 22px; height: 22px; background: var(--brand-blue); }
  .brand-name { font-weight: 700; font-size: 22px; color: var(--ink); letter-spacing: 0.5px; }
  .nav-links { display: flex; gap: 19px; margin-left: auto; list-style: none; font-size: 12.5px; }
  .nav-links a { color: var(--ink-soft); text-decoration: none; }
  .btn-signup {
    margin-left: 22px; display: inline-block; padding: 8px 34px;
    border-radius: 16px; font-size: 12.5px; color: #fff; text-decoration: none;
    background: linear-gradient(90deg, var(--brand-blue) 0%, var(--brand-blue) 22%, var(--brand-red) 45%, var(--brand-red) 70%, var(--brand-orange) 100%);
  }
  .hero-copy { position: relative; text-align: center; margin-top: 170px; }
  .hero-title { font-weight: 400; font-size: 44px; color: var(--ink); letter-spacing: -0.5px; }
  .hero-lead { font-size: 21px; font-weight: 400; color: var(--ink-soft); line-height: 27px; margin-top: 8px; }
  .btn-start {
    display: inline-block; margin-top: 38px; width: 158px; height: 42px; line-height: 38px;
    border: 2px solid var(--ink); border-radius: 21px; font-size: 13px; color: var(--ink-soft);
    text-decoration: none; position: relative; overflow: hidden;
  }
  .btn-start::after {
    content: ""; position: absolute; left: 0; right: 0; bottom: 0; height: 3px;
    background: linear-gradient(90deg, var(--brand-blue), var(--ink) 35%, var(--brand-red) 55%, var(--brand-orange));
  }

  /* Services */
  .services { text-align: center; padding-top: 22px; }
  .section-title { font-weight: 300; font-size: 24px; color: var(--ink); }
  .section-lead { font-size: 11px; color: var(--ink-soft); line-height: 15px; margin-top: 6px; }
  .service-grid { display: flex; justify-content: center; gap: 40px; margin-top: 18px; list-style: none; }
  .service { width: 180px; }
  .service-icon { width: 44px; height: 44px; display: block; margin: 0 auto; }
  .service-name { font-weight: 400; font-size: 14px; color: var(--ink); margin-top: 6px; }
  .service-text { font-size: 10px; line-height: 13px; color: var(--ink-muted); margin-top: 6px; }
  .service-link { display: block; font-size: 10px; color: var(--ink-soft); margin-top: 6px; text-decoration: none; }

  .feature { width: 520px; margin: 22px 0 0 160px; text-align: left; }
  .feature-title { font-weight: 400; font-size: 15px; color: var(--ink); }
  .feature-text { font-size: 11px; line-height: 14px; color: var(--ink-soft); margin-top: 6px; }
</style>
</head>
<body>
<div class="site">
  <header class="hero">
    <div class="hero-photo" role="img" aria-label="Photo of a team collaborating around laptops in a bright office"></div>
    <div class="hero-veil"></div>
    <nav class="nav">
      <div class="brand"><span class="brand-mark"></span><span class="brand-name">Norvex Solutions</span></div>
      <ul class="nav-links">
        <li><a href="#">Products</a></li>
        <li><a href="#">Customers</a></li>
        <li><a href="#">Pricing</a></li>
        <li><a href="#">Developers</a></li>
        <li><a href="#">Support</a></li>
        <li><a href="#">Resources</a></li>
        <li><a href="#">Login</a></li>
      </ul>
      <a class="btn-signup" href="#">Sign Up</a>
    </nav>
    <div class="hero-copy">
      <h1 class="hero-title">We develop software enterprise-level</h1>
      <p class="hero-lead">Lorem ipsum dolor sit amet, consectetur adipiscing elit, sed do eiusmod<br>tempor incididunt ut labore et dolore magna aliqua.</p>
      <a class="btn-start" href="#">Get Started</a>
    </div>
  </header>

  <section class="services">
    <h2 class="section-title">Our services</h2>
    <p class="section-lead">Lorem ipsum dolor sit amet, consectetur adipiscing elit, sed do eiusmod tempor<br>incididunt ut labore et dolore magna aliqua.</p>
    <ul class="service-grid">
      <li class="service">
        <svg class="service-icon" viewBox="0 0 44 44" fill="none" stroke-width="1.4">
          <path stroke="#2c9ad3" d="M19 4h6l1 5 4 2 4-3 4 4-3 4 2 4 5 1v6l-5 1-2 4 3 4-4 4-4-3-4 2-1 5h-6l-1-5-4-2-4 3-4-4 3-4-2-4-5-1v-6l5-1 2-4-3-4 4-4 4 3 4-2z"/>
          <circle cx="22" cy="22" r="5" stroke="#d63e2a"/>
        </svg>
        <h3 class="service-name">Simulation Tools</h3>
        <p class="service-text">Lorem ipsum dolor sit amet, consectetur adipiscing elit, sed do eiusmod tempor.</p>
        <a class="service-link" href="#">Learn More</a>
      </li>
      <li class="service">
        <svg class="service-icon" viewBox="0 0 44 44" fill="none" stroke-width="1.4">
          <rect x="5" y="10" width="34" height="22" stroke="#2c9ad3"/>
          <path stroke="#3d3d3f" d="M2 36h40M16 36v-4h12v4"/>
          <path stroke="#e97f2e" d="M9 27l8-7 6 4 12-14M30 10h5v5"/>
        </svg>
        <h3 class="service-name">Intranet Systems</h3>
        <p class="service-text">Lorem ipsum dolor sit amet, consectetur adipiscing elit, sed do eiusmod tempor.</p>
        <a class="service-link" href="#">Learn More</a>
      </li>
      <li class="service">
        <svg class="service-icon" viewBox="0 0 44 44" fill="none" stroke-width="1.4">
          <rect x="5" y="8" width="34" height="26" stroke="#2c9ad3"/>
          <path stroke="#3d3d3f" d="M5 14h34"/>
          <path stroke="#d63e2a" d="M17 20l-5 4 5 4M27 20l5 4-5 4"/>
        </svg>
        <h3 class="service-name">Hi-tech web presentations</h3>
        <p class="service-text">Lorem ipsum dolor sit amet, consectetur adipiscing elit, sed do eiusmod tempor.</p>
        <a class="service-link" href="#">Learn More</a>
      </li>
      <li class="service">
        <svg class="service-icon" viewBox="0 0 44 44" fill="none" stroke-width="1.4">
          <rect x="8" y="6" width="28" height="10" stroke="#2c9ad3"/>
          <rect x="8" y="19" width="28" height="10" stroke="#2c9ad3"/>
          <path stroke="#e97f2e" d="M22 29v7M12 38h20"/>
          <circle cx="13" cy="11" r="1.5" stroke="#d63e2a"/>
          <circle cx="13" cy="24" r="1.5" stroke="#d63e2a"/>
        </svg>
        <h3 class="service-name">Supporting Enterprise services</h3>
        <p class="service-text">Lorem ipsum dolor sit amet, consectetur adipiscing elit, sed do eiusmod tempor.</p>
        <a class="service-link" href="#">Learn More</a>
      </li>
    </ul>

    <article class="feature">
      <h3 class="feature-title">Optimalization and logistics monitoring</h3>
      <p class="feature-text">Lorem ipsum dolor sit amet, consectetur adipiscing elit, sed do eiusmod tempor incididunt ut labore et dolore magna aliqua. Ut enim ad minim veniam, quis nostrud exercitation ullamco.</p>
    </article>
  </section>
</div>
</body>
</html>
```